Creative Report - A Presentation

We are looking for a report to visual workers' compensation claim data and the impact claims have on premium. I’m looking for something that is very visually new, appealing, easy to understand, and cutting edge.

Right now we are looking for 6 pages to be designed: a cover page, an informative page, and 4 reports. The key data for the last 3 reports are listed in the other document attached named “Key Data for Report”. These should be designed in a 8.5 x 11 page layout.

I would prefer a way where things can be combined without looking too crowded. You can play around with the background, for printing purposes try to leave white space.

Attached are a few graphs that I found that I like the look of. Please design when YOU think is best. The docx & the comments on the side are just to help you visualize.

We are a mod analysis company that is always developing new reports. We are hoping to find a designer we can work with in the future as well – think of this as a trial run!

2 designers reached out this morning wanting to submit designs, I would like to see what they have.

```html
<!DOCTYPE html>
<html lang="en">
<head>
<meta charset="utf-8">
<title>Workers Compensation Executive Summary</title>
<link href="https://fonts.googleapis.com/css2?family=Montserrat:wght@400;500;600;700;800&display=swap" rel="stylesheet">
<style>
:root{
  --navy:#1c3461;
  --blue:#0a97d9;
  --red:#a3281f;
  --green:#8bbd3f;
  --yellow:#e7b416;
  --grey:#c9c9c9;
  --ink:#2b2b2b;
  --stage:#e8e9eb;
  --row:#eeeff2;
}
*{margin:0;padding:0;box-sizing:border-box}
html,body{width:1200px;height:998px;overflow:hidden}
body{background:var(--stage);font-family:"Montserrat",sans-serif;color:var(--ink);position:relative}
.page{position:absolute;width:576px;height:746px;background:#fff;transform:scale(.5714);transform-origin:0 0;box-shadow:0 2px 10px rgba(0,0,0,.12);overflow:hidden}
.p1{left:87px;top:60px}.p2{left:434px;top:60px}.p3{left:783px;top:60px}
.p4{left:87px;top:510px}.p5{left:434px;top:510px}.p6{left:783px;top:510px}
.abs{position:absolute}
.body-text{font-size:10px;line-height:1.35;letter-spacing:-.1px}
h2.page-title{position:absolute;left:40px;top:36px;font-size:19px;font-weight:700;color:#111;letter-spacing:-.2px}
.footer{position:absolute;left:39px;right:40px;top:690px;border-top:1.5px solid #555;padding-top:9px;display:flex;justify-content:space-between;align-items:flex-start}
.footer p{font-size:6px;line-height:1.3;width:450px;color:#333}
.footer .mark{font-size:12px;font-weight:600;color:#bbb;line-height:1;text-align:center}
.footer .mark small{display:block;font-size:4px;letter-spacing:.3px}
/* cover */
.cover-photo{position:absolute;left:0;top:38px;width:576px;height:387px;border-top-left-radius:200px;background:linear-gradient(135deg,#8a6a4f 0%,#c9ccd0 35%,#8fb3d6 60%,#e4e6ea 100%)}
.cover-band{position:absolute;left:0;top:429px;width:576px;height:113px;background:var(--navy);color:#fff;padding:14px 52px}
.cover-band h1{font-size:24px;line-height:1.05;font-weight:700}
.cover-band h1 span{display:block;font-weight:400}
.cover-band hr{border:0;border-top:2px solid #fff;width:64px;margin:6px 0 4px}
.cover-band .eff{font-size:17px}
.cover-band .eff b{font-weight:700}
.agent{position:absolute;left:52px;top:608px;font-size:12px;line-height:1.5}
.agent b{font-weight:700;font-size:11.5px}
.logo-slot{position:absolute;left:394px;top:606px;font-size:20px;font-weight:500}
/* info */
.icons{position:absolute;left:39px;top:133px;display:flex;gap:16px}
.icon-item{width:70px;text-align:center;font-size:6.5px;line-height:1.25}
.icon-box{width:70px;height:70px;border-radius:4px;display:flex;align-items:center;justify-content:center;margin-bottom:12px}
.info-flow{position:absolute;left:39px;top:266px;width:500px}
.info-flow p.body-text{text-align:justify;margin-bottom:11px}
.osha{font-size:15px;line-height:1.3;letter-spacing:-.25px;padding-bottom:8px;margin-bottom:26px;position:relative}
.osha:after{content:"";position:absolute;left:0;bottom:0;width:454px;height:3px;background:#111}
ul.points{list-style:none;font-size:10px;line-height:1.35;margin-bottom:12px}
ul.points li{position:relative;padding-left:36px;margin-bottom:8px}
ul.points li:before{content:"";position:absolute;left:14px;top:5px;width:5px;height:5px;border-radius:50%;background:#111}
/* mod */
.mod-head{font-size:13px;font-weight:700}
.rule{position:absolute;left:45px;width:476px;border-top:1px solid #999}
.good{color:var(--green);font-weight:600}.avg{color:var(--yellow);font-weight:600}.bad{color:var(--red);font-weight:700}
.callout{position:absolute;width:40px;height:40px;border-radius:4px;color:#fff;font-weight:700;font-size:12px;display:flex;align-items:center;justify-content:center}
.tag{position:absolute;font-size:6px;font-weight:700}
/* claims */
.donut-label{font-size:8.5px;line-height:1.3}
.legend{list-style:none;font-size:8px}
.legend li{display:flex;align-items:center;gap:4px}
.legend i{width:6px;height:6px;display:inline-block;flex:none}
table.claims{position:absolute;border-collapse:separate;border-spacing:0;font-size:8.5px;border:2px solid var(--navy);border-radius:6px;overflow:hidden}
table.claims th{background:var(--navy);color:#fff;font-weight:500;font-size:10.5px;height:34px;border-left:1px solid #fff;white-space:nowrap}
table.claims th:first-child{border-left:0;text-align:left;padding-left:10px}
table.claims td{height:17px;text-align:center;border-left:1px solid #fff;line-height:1;white-space:nowrap}
table.claims td:first-child{text-align:left;padding-left:4px;border-left:0;font-size:7.5px}
table.claims tr:nth-child(even) td{background:var(--row)}
.pct{font-size:10px;position:absolute}
</style>
</head>
<body>

<!-- Cover -->
<section class="page p1">
  <div class="cover-photo" role="img" aria-label="Photo of a hand reviewing printed financial charts and reports"></div>
  <div class="cover-band">
    <h1>WORKERS COMPENSATION <span>EXECUTIVE SUMMARY</span></h1>
    <hr>
    <div class="eff"><b>Mod Effective :</b> 10-08-2022</div>
  </div>
  <div class="agent"><b>AGENT INFORMATION</b><br>Name of agent<br>Phone #<br>Email</div>
  <div class="logo-slot">LOGO HERE</div>
</section>

<!-- Info -->
<section class="page p2">
  <p class="abs body-text" style="left:39px;top:38px;width:500px"><span style="color:var(--navy);font-weight:600">Workers compensation</span> claims can have a significant impact on a business. In addition to the direct claim costs, there are many other costs associated with a workers compensation claim that can impact a business.</p>
  <p class="abs body-text" style="left:39px;top:94px">They are:</p>
  <div class="icons">
    <div class="icon-item"><div class="icon-box" style="background:#1a82b8"><svg width="40" height="40" viewBox="0 0 40 40"><circle cx="20" cy="20" r="14" fill="none" stroke="#fff" stroke-width="3"/><text x="20" y="27" text-anchor="middle" fill="#fff" font-size="18" font-weight="700" font-family="Montserrat,sans-serif">$</text></svg></div>Work Comp Premium Costs</div>
    <div class="icon-item"><div class="icon-box" style="background:#5ec3ee"><svg width="40" height="40" viewBox="0 0 40 40"><rect x="8" y="12" width="24" height="15" rx="2" fill="#fff"/><rect x="4" y="28" width="32" height="3" fill="#fff"/><circle cx="31" cy="9" r="5" fill="none" stroke="#fff" stroke-width="2"/></svg></div>Overtime</div>
    <div class="icon-item"><div class="icon-box" style="background:#1b8fdc"><svg width="40" height="40" viewBox="0 0 40 40"><circle cx="20" cy="20" r="15" fill="none" stroke="#fff" stroke-width="4" stroke-dasharray="5 3"/><circle cx="20" cy="17" r="4" fill="#fff"/><path d="M12 28a8 7 0 0 1 16 0z" fill="#fff"/></svg></div>Administrative time spent on claim after an injury</div>
    <div class="icon-item"><div class="icon-box" style="background:#1c3f73"><svg width="40" height="40" viewBox="0 0 40 40"><g stroke="#fff" stroke-width="3"><line x1="20" y1="4" x2="20" y2="36"/><line x1="4" y1="20" x2="36" y2="20"/><line x1="9" y1="9" x2="31" y2="31"/><line x1="31" y1="9" x2="9" y2="31"/></g><circle cx="20" cy="20" r="6" fill="#1c3f73" stroke="#fff" stroke-width="2"/></svg></div>Lost Opportunities due to staffing</div>
    <div class="icon-item"><div class="icon-box" style="background:#1c3461"><svg width="40" height="40" viewBox="0 0 40 40"><circle cx="20" cy="20" r="14" fill="none" stroke="#fff" stroke-width="3"/><rect x="13" y="20" width="3" height="7" fill="#fff"/><rect x="18.5" y="16" width="3" height="11" fill="#fff"/><rect x="24" y="13" width="3" height="14" fill="#fff"/></svg></div>Lost Productivity</div>
    <div class="icon-item"><div class="icon-box" style="background:#29a9e0"><svg width="40" height="40" viewBox="0 0 40 40"><circle cx="20" cy="16" r="9" fill="none" stroke="#fff" stroke-width="3"/><rect x="17" y="24" width="6" height="10" fill="#fff"/><rect x="6" y="30" width="8" height="5" fill="#fff"/></svg></div>Clean up or repair of damaged equipment</div>
  </div>
  <div class="info-flow">
    <p class="osha">OSHA estimates that depending upon the size of the claim indirect costs range from 1 to 4 times the direct costs.</p>
    <p class="body-text">The following report explains in detail how a workers compensation claim affects the premium that your business pays for workers compensation. Most business have an experience mod that is reflective of their past claims experience and every claim has an impact on the experience mod. It is important to note that some claims affect the mod differently.</p>
    <ul class="points">
      <li>A medical only claim is reduced by 70% in the mod calculation.</li>
      <li>A medical/indemnity claim has no reduction.</li>
      <li>All claims are also limited by a primary threshold value where claims are grouped into primary claims and excess claims.</li>
    </ul>
    <p class="body-text">The following report will analyze the types of claims that are occurring in your business and will group them together for ease of identifying trends and areas of opportunity to improve.</p>
    <p class="body-text">By identifying the types and causes of losses many times a cost/benefit analysis can be performed to allow for safety training, additional equipment or building or process improvements.</p>
    <p class="body-text">For the premium cost analysis in this report we have used a manual premium of $XXX,XXX. A manual premium is the premium derived by the carrier before any credits, debits, or experience rating.</p>
  </div>
  <div class="footer"><p>Proprietary and Confidential. Rate Insight provides for an ESTIMATE of an experience modification factor. Your official experience modification factor is issued solely by the applicable workers' compensation rating bureau. Rate Insight Inc. All Rights Reserved.</p><div class="mark">LOGO<small>PLACEHOLDER</small></div></div>
</section>

<!-- Experience mod -->
<section class="page p3">
  <h2 class="page-title" style="left:45px;font-weight:800">YOUR EXPERIENCE MOD</h2>
  <p class="abs" style="left:45px;top:62px;font-size:7px">The report below shows your company's actual experience mod as well as your lowest possible mod.</p>
  <svg class="abs" style="left:0;top:0" width="576" height="260">
    <rect x="86" y="168" width="394" height="12" rx="2" fill="var(--grey)"/>
    <rect x="135" y="168" width="223" height="12" fill="var(--red)"/>
    <g stroke="#555" stroke-width="1"><line x1="86" y1="162" x2="86" y2="186"/><line x1="283" y1="164" x2="283" y2="184"/><line x1="480" y1="162" x2="480" y2="186"/></g>
    <path d="M358 158 L366 158 L358 168z" fill="var(--red)"/>
    <path d="M128 195 L136 182 L136 195z" fill="var(--green)"/>
  </svg>
  <span class="tag" style="left:346px;top:106px;color:var(--red)">Actual Mod</span>
  <div class="callout" style="left:348px;top:118px;background:var(--red)">1.19</div>
  <div class="callout" style="left:108px;top:195px;background:var(--green)">0.63</div>
  <span class="tag" style="left:112px;top:239px;color:var(--green)">Min Mod</span>
  <h3 class="mod-head abs" style="left:45px;top:300px">MOD VALUE EXPLANATION</h3>
  <p class="abs body-text" style="left:45px;top:335px;width:470px;font-size:9px">A mod value <span class="good">below 1.0</span> means your company is <span class="good">performing better</span> than your peers. If your company had no claims your lowest possible mod value would be <span class="good">0.632</span></p>
  <div class="rule" style="top:380px"></div>
  <p class="abs body-text" style="left:45px;top:389px;font-size:9px">A mod of <span class="avg">1.0 is considered average.</span></p>
  <div class="rule" style="top:418px"></div>
  <p class="abs body-text" style="left:45px;top:427px;width:476px;font-size:9px">A mod value <span class="bad">above 1.0</span> means your company is <span class="bad">performing worse</span> than your peers and you will pay more in workers compensation premium.</p>
  <h3 class="abs" style="left:40px;top:496px;font-size:17px;font-weight:700">SUMMARY:</h3>
  <p class="abs body-text" style="left:40px;top:534px;width:496px">The incurred claims reported have a <b>claim impact of .56</b> on your mod value. This is increasing your premium annually by <b>$112,000.</b></p>
  <p class="abs body-text" style="left:40px;top:576px;width:496px">In the following pages we'll dig into the types of claims your business is having and look for areas of opportunity to reduce or eliminate claims and lower your mod value.</p>
  <div class="footer"><p>Proprietary and Confidential. Rate Insight provides for an ESTIMATE of an experience modification factor. Your official experience modification factor is issued solely by the applicable workers' compensation rating bureau. Rate Insight Inc. All Rights Reserved.</p><div class="mark">LOGO<small>PLACEHOLDER</small></div></div>
</section>

<!-- Medical vs indemnity -->
<section class="page p4">
  <h2 class="page-title">MEDICAL VS MEDICAL/INDEMNITY CLAIMS</h2>
  <p class="abs body-text" style="left:40px;top:74px;width:497px;text-align:justify">The type of claims your business is having can have a significant impact on your mod value as not all claims are valued equally. Medical only claims have their value reduced by 70% in the mod calculation and any claim with an indemnity payment is not reduced. This is one of the reasons an effective return to work program can help reduce your premium costs.</p>
  <p class="abs" style="left:40px;top:150px;font-size:11.5px;font-weight:700">Here's your company's breakdown.</p>
  <p class="abs body-text" style="left:40px;top:176px">The total losses for the period reviewed are <b>$284,623.</b><br>Medical only claims accounted for <b>$85,719</b> in losses.<br>Medical/Indemnity claims accounts for <b>$198,904</b> in losses.</p>
  <svg class="abs" style="left:0;top:0" width="576" height="600">
    <circle cx="288" cy="405" r="93" fill="none" stroke="var(--blue)" stroke-width="66"/>
    <circle cx="288" cy="405" r="93" fill="none" stroke="var(--navy)" stroke-width="66" stroke-dasharray="175.3 584.3" transform="rotate(-90 288 405)"/>
    <polyline points="40,325 142,325 172,354" fill="none" stroke="var(--blue)" stroke-width="1.2"/>
    <polyline points="536,325 430,325 400,354" fill="none" stroke="var(--navy)" stroke-width="1.2"/>
    <text x="288" y="400" text-anchor="middle" font-size="40" font-weight="700" fill="#111" font-family="Montserrat,sans-serif">22</text>
    <text x="288" y="437" text-anchor="middle" font-size="20" font-weight="700" fill="#111" font-family="Montserrat,sans-serif">Claims</text>
  </svg>
  <p class="abs donut-label" style="left:40px;top:296px">MEDICAL/<br>INDEMNITY CLAIMS</p>
  <p class="abs donut-label" style="left:40px;top:343px;line-height:2.1"><b>$198,904</b> incurred losses<br><b>0.446</b> mod impact</p>
  <p class="abs donut-label" style="left:40px;top:389px"><b>$267,600</b> 3 yr premium<br>impact</p>
  <p class="abs donut-label" style="right:40px;top:296px;text-align:right">MEDICAL ONLY<br>CLAIMS</p>
  <p class="abs donut-label" style="right:40px;top:343px;text-align:right;line-height:2.1"><b>$85,719</b> incurred losses<br><b>0.127</b>mod impact</p>
  <p class="abs donut-label" style="right:40px;top:389px;text-align:right"><b>$76,200</b> 3 yr premium<br>impact</p>
  <div class="abs" style="left:78px;top:590px;width:21px;height:21px;background:var(--blue)"></div>
  <p class="abs" style="left:120px;top:597px;font-size:8.5px;font-weight:500">MEDICAL/INDEMNITY CLAIMS</p>
  <div class="abs" style="left:327px;top:590px;width:21px;height:21px;background:var(--navy)"></div>
  <p class="abs" style="left:376px;top:597px;font-size:8.5px;font-weight:500">MEDICAL ONLY CLAIMS</p>
  <div class="footer"><p>Proprietary and Confidential. Rate Insight provides for an ESTIMATE of an experience modification factor. Your official experience modification factor is issued solely by the applicable workers' compensation rating bureau. Rate Insight Inc. All Rights Reserved.</p><div class="mark">LOGO<small>PLACEHOLDER</small></div></div>
</section>

<!-- Cause of injury -->
<section class="page p5">
  <h2 class="page-title">CLAIMS BY CAUSE OF INJURY</h2>
  <p class="abs body-text" style="left:40px;top:74px;width:497px;text-align:justify">Visually grouping the claims together can help with identifying trends and areas to focus on for improvement and future risk management. The following groupings identify the top losses incurred by your company.</p>
  <svg class="abs" style="left:0;top:0" width="576" height="420">
    <ellipse cx="214" cy="286" rx="107" ry="107" fill="#555" opacity=".35"/>
    <path d="M214 282 L214 175 A107 107 0 0 1 320.9 278.3Z" fill="#4a75ad" stroke="#fff" stroke-width=".6"/>
    <path d="M214 282 L320.9 278.3 A107 107 0 0 1 195.4 387.4Z" fill="#a84443" stroke="#fff" stroke-width=".6"/>
    <path d="M214 282 L195.4 387.4 A107 107 0 0 1 117 327.2Z" fill="#86a54a" stroke="#fff" stroke-width=".6"/>
    <path d="M214 282 L117 327.2 A107 107 0 0 1 160.5 189.3Z" fill="#785e97" stroke="#fff" stroke-width=".6"/>
    <path d="M214 282 L160.5 189.3 A107 107 0 0 1 186.3 178.6Z" fill="#4596ac" stroke="#fff" stroke-width=".6"/>
    <path d="M214 282 L186.3 178.6 A107 107 0 0 1 214 175Z" fill="#d98a41" stroke="#fff" stroke-width=".6"/>
  </svg>
  <ul class="legend abs" style="left:362px;top:186px;font-size:7px;line-height:1.3">
    <li style="align-items:flex-start;height:28px"><i style="background:#4a75ad;margin-top:2px"></i>Fall, Slip or Trip Injury Cut,<br>Puncture, Scrape</li>
    <li style="height:28px;align-items:flex-start"><i style="background:#a84443;margin-top:2px"></i>Injured By</li>
    <li style="height:28px;align-items:flex-start"><i style="background:#86a54a;margin-top:2px"></i>Struck or Injured By</li>
    <li style="height:28px;align-items:flex-start"><i style="background:#785e97;margin-top:2px"></i>Strain or Injury By</li>
    <li style="height:28px;align-items:flex-start"><i style="background:#4596ac;margin-top:2px"></i>Motor Vehicle</li>
    <li style="height:28px;align-items:flex-start"><i style="background:#d98a41;margin-top:2px"></i>Burn or Scald</li>
    <li style="align-items:flex-start"><i style="background:#8fa6cf;margin-top:2px"></i>Miscellaneous Causes</li>
  </ul>
  <table class="claims" style="left:33px;top:474px;width:508px">
    <tr><th style="width:100px">Claim Type</th><th style="width:80px"># of Claims</th><th style="width:106px">Claim Amount</th><th style="width:88px">Mod Impact</th><th>3 year Premium Cost</th></tr>
    <tr><td style="line-height:1.1">Fall, Slip or Trip Injury<br>Cut, Puncture, Scrape</td><td>4</td><td>$81,879</td><td>0.137</td><td>$82,200</td></tr>
    <tr><td>Injured By</td><td>3</td><td>$73,917</td><td>0.130</td><td>$11,400</td></tr>
    <tr><td>Struck or Injured By</td><td>4</td><td>$58,108</td><td>0.087</td><td>$87,600</td></tr>
    <tr><td>Strain or Injury By</td><td>4</td><td>$35,669</td><td>0.146</td><td>$52,200</td></tr>
    <tr><td>Motor Vehicle</td><td>2</td><td>$23,674</td><td>0.032</td><td>$19,200</td></tr>
    <tr><td>Burn or Scald</td><td>4</td><td>$10,426</td><td>0.039</td><td>$23,400</td></tr>
    <tr><td>Miscellaneous Causes</td><td>1</td><td>$950</td><td>0.002</td><td>$1,200</td></tr>
  </table>
  <div class="footer"><p>Proprietary and Confidential. Rate Insight provides for an ESTIMATE of an experience modification factor. Your official experience modification factor is issued solely by the applicable workers' compensation rating bureau. Rate Insight Inc. All Rights Reserved.</p><div class="mark">LOGO<small>PLACEHOLDER</small></div></div>
</section>

<!-- Nature of injury -->
<section class="page p6">
  <h2 class="page-title">CLAIMS BY NATURE OF INJURY</h2>
  <svg class="abs" style="left:0;top:0" width="576" height="400">
    <ellipse cx="176" cy="245" rx="102" ry="102" fill="#2b3550"/>
    <path d="M176 242 L176 140 A102 102 0 0 1 213.5 147.2Z" fill="#4a75ad" stroke="#fff" stroke-width=".6"/>
    <path d="M176 242 L213.5 147.2 A102 102 0 0 1 225.1 152.6Z" fill="#a84443" stroke="#fff" stroke-width=".6"/>
    <path d="M176 242 L225.1 152.6 A102 102 0 0 1 230.7 155.9Z" fill="#86a54a" stroke="#fff" stroke-width=".6"/>
    <path d="M176 242 L230.7 155.9 A102 102 0 0 1 262.1 187.3Z" fill="#6a4f8a" stroke="#fff" stroke-width=".6"/>
    <path d="M176 242 L262.1 187.3 A102 102 0 0 1 230.7 328.1Z" fill="#3d8fa6" stroke="#fff" stroke-width=".6"/>
    <path d="M176 242 L230.7 328.1 A102 102 0 0 1 229.1 329.1Z" fill="#d98a41"/>
    <path d="M176 242 L229.1 329.1 A102 102 0 0 1 78.5 271.8Z" fill="#8fa6cf" stroke="#fff" stroke-width=".6"/>
    <path d="M176 242 L78.5 271.8 A102 102 0 0 1 76.2 221.1Z" fill="#d79a98" stroke="#fff" stroke-width=".6"/>
    <path d="M176 242 L76.2 221.1 A102 102 0 0 1 81.8 202.8Z" fill="#bcd39a" stroke="#fff" stroke-width=".6"/>
    <path d="M176 242 L81.8 202.8 A102 102 0 0 1 176 140Z" fill="#a99cc4" stroke="#fff" stroke-width=".6"/>
  </svg>
  <span class="pct" style="left:176px;top:148px">6%</span>
  <span class="pct" style="left:206px;top:127px">2%</span>
  <span class="pct" style="left:230px;top:134px">1%</span>
  <span class="pct" style="left:226px;top:170px">7%</span>
  <span class="pct" style="left:251px;top:247px">25%</span>
  <span class="pct" style="left:130px;top:311px">29%</span>
  <span class="pct" style="left:233px;top:335px">0%</span>
  <span class="pct" style="left:71px;top:240px">8%</span>
  <span class="pct" style="left:54px;top:200px">3%</span>
  <span class="pct" style="left:118px;top:164px">19%</span>
  <ul class="legend abs" style="left:357px;top:135px;font-size:9.5px;line-height:22.5px">
    <li><i style="background:#4a75ad"></i>All Other Specific Injuries, NOC</li>
    <li><i style="background:#a84443"></i>Bruising</li>
    <li><i style="background:#86a54a"></i>Burn or Scald</li>
    <li><i style="background:#6a4f8a"></i>Concussion</li>
    <li><i style="background:#3d8fa6"></i>Crushing</li>
    <li><i style="background:#d98a41"></i>Heat Prostration</li>
    <li><i style="background:#8fa6cf"></i>Laceration</li>
    <li><i style="background:#d79a98"></i>Poisoning</li>
    <li><i style="background:#bcd39a"></i>Sprain or Tear</li>
    <li><i style="background:#a99cc4"></i>Strain or Tear</li>
  </ul>
  <table class="claims" style="left:33px;top:451px;width:509px">
    <tr><th style="width:98px">Claim Type</th><th style="width:78px"># of Claims</th><th style="width:110px">Claim Amount</th><th style="width:88px">Mod Impact</th><th>3 year Premium Cost</th></tr>
    <tr><td style="line-height:1.1">All Other Specific<br>Injuries, NOC</td><td>1</td><td>$18,500</td><td>0.025</td><td>$15,000</td></tr>
    <tr><td>Bruising</td><td>2</td><td>$7,759</td><td>0.011</td><td>$6,600</td></tr>
    <tr><td>Burn or Scald</td><td>2</td><td>$2,990</td><td>0.005</td><td>$3,000</td></tr>
    <tr><td>Concussion</td><td>2</td><td>$22,991</td><td>0.031</td><td>$18,600</td></tr>
    <tr><td>Crushing</td><td>2</td><td>$34,115</td><td>0.113</td><td>$67,800</td></tr>
    <tr><td>Heat Prostration</td><td>1</td><td>$950</td><td>0.002</td><td>$1,200</td></tr>
    <tr><td>Laceration</td><td>3</td><td>$73,917</td><td>0.13</td><td>$78,000</td></tr>
    <tr><td>Poisoning</td><td>1</td><td>$7,436</td><td>0.034</td><td>$20,400</td></tr>
    <tr><td>Sprain or Tear</td><td>2</td><td>$5,296</td><td>0.015</td><td>$9,000</td></tr>
    <tr><td>Strain or Tear</td><td>5</td><td>$110,669</td><td>0.087</td><td>$52,200</td></tr>
  </table>
  <div class="footer"><p>Proprietary and Confidential. Rate Insight provides for an ESTIMATE of an experience modification factor. Your official experience modification factor is issued solely by the applicable workers' compensation rating bureau. Rate Insight Inc. All Rights Reserved.</p><div class="mark">LOGO<small>PLACEHOLDER</small></div></div>
</section>

</body>
</html>
```